Every Shelf Neatly Sorted or ESN Organized needs a business card design. ESN Organized is a professi

We need a business card design that is clean, sharp and conveys a sense of organization. I already have a logo.

Reason: I am still providing feedback and need more time.

Target Market(s)

Families (specifically mothers), small business owners, parents, seniors

Industry/Entity Type

Business

Contact Information for Business Card

My website is www.esnsortedhome.example and my Facebook page is http://www.facebook.example/everyshelfneatlysorted. The phone number is 555-418-2706 and I want to be listed as Marla V. Osgood, Owner

Requirements
Must have
• My logo.

```html
<!DOCTYPE html>
<html lang="en">
<head>
<meta charset="utf-8">
<title>Every Shelf Neatly Sorted — Business Card</title>
<link rel="stylesheet" href="https://fonts.googleapis.com/css2?family=Arimo:wght@400;700&display=swap">
<style>
  :root {
    --page-bg: #e9e6e1;
    --card-black: #0b0b0b;
    --card-white: #ffffff;
    --brand-blue: #1a86d9;
    --text-white: #ffffff;
    --text-dark: #1b1b1b;
    --muted-white: #cfcfcf;
  }
  * { box-sizing: border-box; margin: 0; padding: 0; }
  html, body { width: 1200px; height: 950px; overflow: hidden; }
  body {
    background: var(--page-bg);
    position: relative;
    font-family: "Arimo", Arial, sans-serif;
  }
  .card {
    position: absolute;
    left: 250px;
    width: 700px;
    height: 400px;
    border-radius: 4px;
    box-shadow: 0 10px 28px rgba(0,0,0,0.25);
    overflow: hidden;
  }
  /* Front */
  .card-front {
    top: 50px;
    background: linear-gradient(160deg, #1c1c1c 0%, var(--card-black) 45%, #000 100%);
  }
  .card-front .brand-name {
    position: absolute;
    left: 150px;
    top: 150px;
    font-family: "Arimo", sans-serif;
    font-weight: 400;
    font-size: 40px;
    color: var(--text-white);
  }
  .card-front .web {
    position: absolute;
    left: 152px;
    top: 232px;
    font-family: "Arimo", sans-serif;
    font-size: 17px;
    letter-spacing: 6px;
    color: var(--muted-white);
  }
  /* Back */
  .card-back {
    top: 500px;
    background: var(--card-white);
  }
  .card-back .edge-bar {
    position: absolute;
    left: 40px;
    top: 0;
    width: 16px;
    height: 210px;
    background: var(--card-black);
  }
  .card-back .brand-name {
    position: absolute;
    left: 95px;
    top: 82px;
    font-family: "Arimo", sans-serif;
    font-weight: 400;
    font-size: 26px;
    color: var(--text-dark);
  }
  .contact-panel {
    position: absolute;
    left: 335px;
    top: 130px;
    right: 0;
    height: 225px;
    background: var(--brand-blue);
    border-radius: 48px 0 0 48px;
    color: var(--text-white);
    padding: 30px 0 0 48px;
  }
  .contact-panel .person-name {
    font-weight: 700;
    font-size: 25px;
    letter-spacing: 0.5px;
    text-transform: uppercase;
  }
  .contact-panel .person-role {
    margin-top: 4px;
    font-weight: 700;
    font-size: 15px;
    text-transform: uppercase;
  }
  .contact-list {
    list-style: none;
    margin-top: 26px;
  }
  .contact-list li {
    display: flex;
    align-items: center;
    gap: 10px;
    font-size: 19px;
    line-height: 27px;
  }
  .contact-list svg { width: 17px; height: 17px; flex: none; }
</style>
</head>
<body>
  <section class="card card-front" aria-label="Business card front">
    <div class="brand-name">Every Shelf Neatly Sorted</div>
    <div class="web">www.esnsortedhome.example</div>
  </section>

  <section class="card card-back" aria-label="Business card back">
    <div class="edge-bar"></div>
    <div class="brand-name">Every Shelf Neatly Sorted</div>
    <div class="contact-panel">
      <div class="person-name">Marla V. Osgood</div>
      <div class="person-role">Owner</div>
      <ul class="contact-list">
        <li>
          <svg viewBox="0 0 24 24" aria-hidden="true"><path fill="#fff" d="M6.6 10.8a15.1 15.1 0 0 0 6.6 6.6l2.2-2.2c.3-.3.7-.4 1-.2 1.1.4 2.3.6 3.6.6.6 0 1 .4 1 1V20c0 .6-.4 1-1 1A17 17 0 0 1 3 4c0-.6.4-1 1-1h3.5c.6 0 1 .4 1 1 0 1.3.2 2.5.6 3.6.1.3 0 .7-.2 1z"/></svg>
          555-418-2706
        </li>
        <li>
          <svg viewBox="0 0 24 24" aria-hidden="true"><circle cx="12" cy="12" r="9" fill="none" stroke="#fff" stroke-width="2.4"/><path d="M3 12h18M12 3c3 3 3 15 0 18M12 3c-3 3-3 15 0 18" fill="none" stroke="#fff" stroke-width="1.8"/></svg>
          www.esnsortedhome.example
        </li>
        <li>
          <svg viewBox="0 0 24 24" aria-hidden="true"><circle cx="12" cy="12" r="9" fill="#fff"/></svg>
          everyshelfneatlysorted
        </li>
      </ul>
    </div>
  </section>
</body>
</html>
```